Harbourline Sonography Academy (Kestrel Institute of Clinical Scanning) needs an additional web design f

Don't require a redesign of our existing website, I need an additional web design to compliment and feed into our existing web page (kics.edu.au) but establish excellent zintro rankings in it's own right. Web page is to appeal to a specific target market in the allied health industry who wish to learn how to do ultrasound on patients. New website is www. frontlinescanskills.com.au. Our educational institution delivers hands on workshops and seminars on ANYTHING involved with EMERGENCY Ultrasound - intro, advanced, doctors, nurses, etc. Our competitors in this field www.bedsidewavelabs.com.au and www.qpo.edu.au. Looking for a design that will capture the target audience and deliver the message that the courses are delivered by one of the best faculties in Australia. SEO strategies are paramount in that we don't wish to be penalised by Zintro by running a feeder site. Courses are delivered in Sydney and are accredited by an organisation called BRAV.com.au. The courses are listed under 2 qualifications on BRAV website - DLTX and KMRTE. Registrants of our courses are striving to achieve either DLTX - Certificate in Bedside Operator Sonography http://www.brav.com.au/newsite/Files/Documents/Education/DLTX/DLTX_Course_Brochure.pdf OR KMRTE - Certificate in Support Staff Operated Echography http://www.brav.com.au/newsite/Files/Documents/Education/KMRTE/KMRTE_Course_Brochure.pdf.
Website to be lumofon, smartphone and tablet compatible.

Target Market(s)

Emergency Physicians and Emergency nurses/doctors.

Industry/Entity Type

School

Coding

Coded - Design and coding required

Number of Pages Required

2 page

Other font styles liked:
• See website http://www.oakpointdental.com.au/

Colors
86cae6
ec1f27

Requirements
Must have
• Overall professional feel but easy to read and informative.
• Links to our normal website pages www.kics.edu.au
• Ability to rank high.
• Copy of material we deliver here http://www.kics.edu.au/emergency-ultrasound-course-1-3-days/ Click through on relevant dates for more information.
Nice to have
• I like this website - font, feel, layout etc.
• http://www.oakpointdental.com.au/
Should not have
• Information that will lower our zintro rankings knowing it is linked to www.kics.edu.au

```html
<!DOCTYPE html>
<html lang="en">
<head>
<meta charset="utf-8">
<title>Frontline Scan Skills – Ultrasound Training Specialists</title>
<link rel="stylesheet" href="https://fonts.googleapis.com/css2?family=Open+Sans:wght@300;400;600;700&display=swap">
<style>
:root{
  --blue:#0a4fa6;
  --blue-dark:#0b3f86;
  --sky:#86cae6;
  --red:#e0232b;
  --red-btn:#e52a30;
  --ink:#333;
  --panel:#f4f4f4;
  --footer:#4a4a4a;
  --footer-base:#3d3d3d;
  --white:#fff;
}
*{box-sizing:border-box;margin:0;padding:0}
html,body{width:1200px;height:2206px;overflow:hidden}
body{font-family:"Open Sans",Arial,sans-serif;color:var(--ink);background:var(--white);position:relative}
a{text-decoration:none;color:inherit}

/* header */
.site-header{position:absolute;left:0;top:0;width:1200px;height:166px;background:var(--white)}
.brand{position:absolute;left:100px;top:20px;font-size:38px;line-height:39px;font-weight:400;color:var(--blue)}
.tagline{position:absolute;right:102px;top:30px;font-size:27px;font-weight:300;color:#aaa}
.social{position:absolute;left:691px;top:90px;display:flex;gap:9px}
.social span{width:32px;height:32px;border-radius:50%;display:block}
.search{position:absolute;left:865px;top:91px;width:233px;height:33px;border:1px solid #ccc;background:#fff;font-size:13px;color:#888;padding:7px 12px}
.search svg{position:absolute;right:8px;top:8px}

/* nav */
.main-nav{position:absolute;left:0;top:166px;width:1200px;height:53px;background:var(--blue)}
.main-nav a{position:absolute;top:0;height:53px;line-height:53px;font-size:14.5px;font-weight:600;color:var(--white)}
.main-nav a.active{background:var(--sky);padding:0 22px;left:100px}

/* hero */
.hero{position:absolute;left:0;top:219px;width:1200px;height:440px;background:linear-gradient(90deg,#f3f5f8 0%,#eef1f5 40%,#e9edf2 100%)}
.hero-photo{position:absolute;left:470px;top:0;width:730px;height:440px;background:linear-gradient(120deg,#eef1f4 0%,#f1e4da 45%,#f2f2f2 70%,#dfe6ee 100%)}
.hero h1{position:absolute;left:128px;top:100px;font-size:39.5px;font-weight:600;color:var(--blue-dark)}
.hero p{position:absolute;left:128px;top:152px;font-size:19px;line-height:28px;color:#444}
.btn{display:inline-block;color:var(--white);font-weight:400;text-align:center}
.hero .btn{position:absolute;left:128px;top:222px;width:203px;height:47px;line-height:47px;background:var(--red-btn);font-size:19px;border-radius:2px}
.hero-arrows{position:absolute;left:128px;top:290px;display:flex;gap:7px}

/* feature cards */
.card{position:absolute;top:709px;width:311px;text-align:center}
.card .thumb{width:311px;height:178px;box-shadow:0 4px 5px rgba(0,0,0,.18)}
.card h3{margin-top:16px;font-size:23px;font-weight:400}
.card p{margin-top:4px;font-size:14px;color:#555}
.divider{position:absolute;left:100px;top:1006px;width:1000px;height:1px;background:#ddd}

/* intro */
.intro{position:absolute;left:0;top:1046px;width:1200px;text-align:center}
.intro h2{font-size:36px;font-weight:300;color:var(--blue)}
.intro .sub{margin-top:6px;font-size:16.5px;color:#555;letter-spacing:.2px}
.intro .lead{margin:10px auto 0;width:880px;font-size:18.8px;line-height:27px;color:var(--blue)}
.intro .cta{margin-top:9px;font-size:23px;font-weight:700;color:var(--red)}
.ticket-row{display:flex;justify-content:center;gap:18px;margin-top:10px}
.ticket-row .btn{height:49px;line-height:49px;font-size:18.5px;border-radius:2px;box-shadow:0 2px 2px rgba(0,0,0,.2)}
.ticket-red{width:338px;background:var(--red-btn)}
.ticket-dark{width:348px;background:#444}

/* course panel */
.courses{position:absolute;left:0;top:1347px;width:1200px;height:524px;background:var(--panel)}
.course{position:absolute;top:36px}
.course h4{font-size:18.5px;line-height:25px;font-weight:600;color:var(--red)}
.course ul{list-style:none;margin-top:24px}
.course li{font-size:14.5px;line-height:29.4px;color:#555}
.course li::before{content:"·";margin-right:8px;color:#777}
.echo{width:391px;height:128px;margin-top:6px;background:linear-gradient(90deg,#1d1d1d,#4a4a4a 50%,#222)}
.book{position:absolute;top:324px}
.book h5{font-size:23px;font-weight:400;color:#333}
.book a{display:block;margin-top:16px;font-size:16.8px;color:var(--blue)}
.book h5+a{margin-top:16px}

/* footer */
.site-footer{position:absolute;left:0;top:1871px;width:1200px;height:251px;background:var(--footer)}
.foot-col{position:absolute;top:46px}
.foot-col h6{font-size:19px;font-weight:400;color:var(--white)}
.foot-col a,.foot-col span{display:block;font-size:13.5px;line-height:25px;color:#ccc}
.foot-col h6+*{margin-top:8px}
.footer-base{position:absolute;left:0;top:2122px;width:1200px;height:84px;background:var(--footer-base)}
.copyright{position:absolute;left:101px;top:35px;font-size:12px;color:#ccc}
.foot-social{position:absolute;left:945px;top:26px;display:flex;gap:9px}
.foot-social span{width:32px;height:32px;border-radius:50%;background:#8a8a8a;display:block}
</style>
</head>
<body>

<header class="site-header">
  <a class="brand" href="#">Frontline<br>Scan<br>Skills</a>
  <div class="tagline">Ultrasound Training Specialists</div>
  <div class="social" aria-label="Social links">
    <span style="background:#1f5fb0"></span>
    <span style="background:#2aa7e0"></span>
    <span style="background:#dd4b32"></span>
    <span style="background:#cc2a24"></span>
  </div>
  <div class="search">Search
    <svg width="16" height="16" viewBox="0 0 16 16"><circle cx="6" cy="6" r="4.5" fill="none" stroke="#333" stroke-width="2"/><line x1="9.5" y1="9.5" x2="14" y2="14" stroke="#333" stroke-width="2.5"/></svg>
  </div>
</header>

<nav class="main-nav">
  <a class="active" href="#">ABOUT FSS</a>
  <a href="#" style="left:244px">SEMINARS</a>
  <a href="#" style="left:362px">BECOME A SONOGRAPHER</a>
  <a href="#" style="left:594px">CONSULTING</a>
  <a href="#" style="left:734px">MODELS</a>
  <a href="#" style="left:838px">INFORMATION</a>
  <a href="#" style="left:987px">CONTACT US</a>
</nav>

<section class="hero">
  <div class="hero-photo" role="img" aria-label="Photo of an expectant mother lying back during an ultrasound scan"></div>
  <h1>Interested?</h1>
  <p>Find a Seminar or Course and register<br>with Frontline Scan Skills</p>
  <a class="btn" href="#">REGISTER ONLINE</a>
  <div class="hero-arrows">
    <svg width="25" height="25" viewBox="0 0 25 25"><circle cx="12.5" cy="12.5" r="12.5" fill="#999"/><path d="M14.5 7.5 9.5 12.5 14.5 17.5" fill="none" stroke="#fff" stroke-width="2.5"/></svg>
    <svg width="25" height="25" viewBox="0 0 25 25"><circle cx="12.5" cy="12.5" r="12.5" fill="#999"/><path d="M10.5 7.5 15.5 12.5 10.5 17.5" fill="none" stroke="#fff" stroke-width="2.5"/></svg>
  </div>
</section>

<article class="card" style="left:101px">
  <div class="thumb" role="img" aria-label="Photo of a sonographer beside an ultrasound machine" style="background:linear-gradient(135deg,#e9d8c8,#cfdbe6 55%,#7f93a8)"></div>
  <h3 style="color:var(--red)">SEMINARS</h3>
  <p>Earn CPO points with KICS</p>
</article>
<article class="card" style="left:446px">
  <div class="thumb" role="img" aria-label="Photo of an expectant mother viewing an ultrasound print" style="background:linear-gradient(135deg,#eeeeee,#d9d3cc 55%,#b9a99a)"></div>
  <h3 style="color:var(--blue-dark)">STUDY AT FSS</h3>
  <p>Graduate program in medical Ultrasound</p>
</article>
<article class="card" style="left:788px">
  <div class="thumb" role="img" aria-label="Photo of an expectant mother holding ultrasound images" style="background:linear-gradient(135deg,#f4f4f4,#e6ddd4 55%,#9c8574)"></div>
  <h3 style="color:#2aa7d8">APPLY TO BE A MODEL</h3>
  <p>Help KICS by applying to a model</p>
</article>

<div class="divider"></div>

<section class="intro">
  <h2>Emergency Ultrasound Course</h2>
  <p class="sub">KESTREL INSTITUTE OF CLINICAL SCANNING AND ULTRASOUND VILLAGE</p>
  <p class="lead">Donec nisl augue, pulvinar in sapien et, molestie lobortis risus. Praesent sed enim at neque sagittis aliquet non faucibus felis. Etiam pulvinar urna diam, dictum sodales nibh.</p>
  <p class="cta">BUY SEMINAR TICKETS FOR</p>
  <div class="ticket-row">
    <a class="btn ticket-red" href="#">BUY DLTX SEMINAR TICKET NOW</a>
    <a class="btn ticket-dark" href="#">BUY KMRTE SEMINAR TICKET NOW</a>
  </div>
</section>

<section class="courses">
  <div class="course" style="left:137px">
    <h4>EMERGENCY ULTRASOUND COURSE<br>2 DAYS</h4>
    <ul>
      <li>ULTRASOUND ESSENTIALS</li>
      <li>ABDOMINAL AORTIC ANEURYSM (AAA)</li>
      <li>E-FAST</li>
      <li>VASCULAR ACCESS</li>
      <li>FOREIGN BODIES</li>
      <li>DVT</li>
    </ul>
  </div>
  <div class="course" style="left:659px">
    <h4>EMERGENCY ULTRASOUND COURSE<br>1 DAY Add on option</h4>
    <ul>
      <li>BASIC ECHOCARDIOGRAPHY IN LIFE SUPPORT (BELS)</li>
    </ul>
    <div class="echo" role="img" aria-label="Greyscale ultrasound scan image" style="margin-left:-3px"></div>
  </div>
  <div class="book" style="left:133px">
    <h5>Book this Seminar :</h5>
    <a href="#">29/01/2015 from 8:00 AM to 30/01/2015 3:00 PM</a>
    <a href="#">14/05/2015 from 8:00 AM to 15/05/2015 3:00 PM</a>
    <a href="#">03/09/2015 from 8:00 AM to 04/09/2015 3:00 PM</a>
  </div>
  <div class="book" style="left:655px">
    <h5>Book this Seminar :</h5>
    <a href="#">31/01/2015 from 8:00 AM to 31/01/2015 3:50 PM</a>
    <a href="#">16/05/2015 from 8:00 AM to 16/05/2015 3:50 PM</a>
    <a href="#">05/09/2015 from 8:00 AM to 05/09/2015 3:50 PM</a>
  </div>
</section>

<footer class="site-footer">
  <div class="foot-col" style="left:135px">
    <h6>ABOUT KICS</h6>
    <a href="#">About Us</a><a href="#">Our Guarantee</a><a href="#">Facilities</a><a href="#">History</a><a href="#">Privacy Policy</a>
  </div>
  <div class="foot-col" style="left:334px">
    <h6>SONOGRAPHY</h6>
    <a href="#">CPSV Program Overview</a><a href="#">TRLP Program Overview</a><a href="#">TRLP Trainee Testimonials</a><a href="#">Meet some past students</a>
  </div>
  <div class="foot-col" style="left:604px">
    <h6>INFORMATION</h6>
    <a href="#">Accommodation</a><a href="#">Local Information</a><a href="#">Useful Links</a><a href="#">Venue Information</a>
  </div>
  <div class="foot-col" style="left:824px">
    <h6>CONTACT US</h6>
    <span>Suite 208, Meridian House 14 Larkspur Rd</span>
    <span>Westmead Vale NSW, 2199</span>
    <span>Phone: + 61 2 5550 1842</span>
    <span>Fax: + 61 2 5550 1843</span>
    <span>Email: admin@fss.edu.au</span>
  </div>
</footer>

<div class="footer-base">
  <p class="copyright">Copyright 2014 Frontline Scan Skills. All rights reserved.</p>
  <div class="foot-social" aria-label="Social links"><span></span><span></span><span></span><span></span></div>
</div>

</body>
</html>
```